The Quiet Harvest Book Cover

Cover for Multiauthor Ebook & Paper Print Book Cover

Book Title:
The Quiet Harvest: Field Notes Gathered By Many Guides for Thriving on Every Road Ahead

This book will offer the wisdom and philosophies of a variety of different coaches to allow future clients to get a taste of you and your style and prepare them to work with you!

A coach does not fix you. Or heal you. They coach you - offer thoughts to ponder, guidance, techniques to try. All to help you plays and succeed at the game of life.

Each coach has their own personality, training, experience, method and philosophy they bring to the table. The underlying purpose is to guide you through the quiet harvest, to become the person you desire and aspire to be. Different coaches for different folks, yet they all have their own unique wisdom and special sauce to share.

This book is a collection of just that. A tasting of the wisdom and philosophies of a variety of different coaches for you to experience.

Types of Coaches: Clarity, Dreams, Goals, Motivation, Mindset,  Subconscious, Beliefs, Behavior, Accountability, Life, Wellness, Love & Dating, Relationships, Sex, Business, Career,  Executive,  Personal Development,  Writing, Wellness, Fitness, Parenting,  Style, Spirituality, Public Speaking, Financial,  Time management, Weight Loss, Running, Self esteem,  Tarot, Astrology, Enneagram, Soul path/ Dharma, Skills, Performance,  Speaking / Communication, Leadership, Shadow Work, Acting, Sports, ANY & ALL

Target Market(s)

Males or females looking for guidance and words of wisdom from an expert coach - maybe to find one that resonates with them to work with further. Ages 16 and up. Any Gender. International. Looking to improve their life!

Industry/Entity Type

Self Development, Wellness, Coaching, Personal Growth, Fitness, Spirituality, Business, Relationships

Font styles to use
Serif
Script

Colors
0054AA
0677BA
7BADD7
CADEEF
E8F1F8
FFF300
FFF600
FEFA6F
FFFEC7
FFFEE8

Requirements
Must have
• I am looking for a visually appealing, unique cover that encompasses the breadth and depth of the transformation that people can go through and inspires them to want to grow and change even more. I love when elegant and classic simplicity is combined with some kind of twist that catches the eye and provokes thought. I love complimentary fonts, colors, design elements. You can visit my Bramblo Author Page - Dr. Marguerite Oslan Pardevy to see my titles to see what I have liked! But I am also excited to see where you can make my vision even better!!
Nice to have
• Front Cover - Image, Title and Subtitle, The Lantern Gate Publishing House, Spine - Title and Publishing House Logo, Back - Book Blurb, Authors Names, Info about Publishing House, ISBN Barcode
Should not have
• Anything too feminine or too masculine as I want to encourage coaches of all genders to participate.

```html
<!DOCTYPE html>
<html lang="en">
<head>
<meta charset="utf-8">
<title>The Quiet Harvest — Book Cover</title>
<link rel="stylesheet" href="https://fonts.googleapis.com/css2?family=Great+Vibes&family=Playfair+Display:wght@600;700&display=swap">
<style>
  :root {
    --stage: #4a4a4d;
    --paper: #ffffff;
    --inner-disc: #fffee8;
    --ink: #0054aa;
    --ink-soft: #0677ba;
    --sky: #7badd7;
    --mist: #cadeef;
    --frost: #e8f1f8;
    --sun: #fff300;
    --lemon: #fff600;
    --butter: #fefa6f;
    --cream: #fffec7;
  }
  * { box-sizing: border-box; margin: 0; padding: 0; }
  html, body {
    width: 882px;
    height: 1200px;
    overflow: hidden;
    background: var(--stage);
  }
  .cover {
    position: absolute;
    left: 56px;
    top: 24px;
    width: 770px;
    height: 1152px;
    background: var(--paper);
    overflow: hidden;
  }
  .cover-art {
    position: absolute;
    inset: 0;
    width: 100%;
    height: 100%;
  }
  .title-block {
    position: absolute;
    left: 120px;
    width: 530px;
    top: 410px;
    text-align: center;
    color: var(--ink);
  }
  .book-title {
    font-family: "Playfair Display", Georgia, serif;
    font-weight: 700;
    font-size: 66px;
    line-height: 1.02;
    text-transform: uppercase;
    letter-spacing: 1px;
  }
  .book-title .lead {
    display: block;
    font-family: "Great Vibes", cursive;
    font-weight: 400;
    font-size: 64px;
    line-height: 0.9;
    text-transform: none;
    letter-spacing: 0;
    color: var(--ink-soft);
  }
  .book-subtitle {
    width: 390px;
    margin: 26px auto 0;
    font-family: "Playfair Display", Georgia, serif;
    font-weight: 600;
    font-size: 17px;
    line-height: 1.65;
    text-transform: uppercase;
    letter-spacing: 0.6px;
  }
  .publisher {
    position: absolute;
    left: 0;
    right: 0;
    top: 1088px;
    text-align: center;
    color: var(--ink);
    font-family: "Playfair Display", Georgia, serif;
    font-weight: 700;
    font-size: 23px;
    letter-spacing: 1px;
    text-transform: uppercase;
  }
</style>
</head>
<body>
  <main class="cover">
    <svg class="cover-art" viewBox="0 0 770 1152" role="img"
         aria-label="Watercolour ring in deep and pale blues surrounding a cream disc, with painted butterflies in blue and sunny yellow drifting around it">
      <defs>
        <radialGradient id="ring-wash" cx="0.5" cy="0.5" r="0.5">
          <stop offset="0.7" stop-color="#0677ba"/>
          <stop offset="0.86" stop-color="#7badd7"/>
          <stop offset="1" stop-color="#cadeef" stop-opacity="0"/>
        </radialGradient>
        <radialGradient id="frost-wash" cx="0.5" cy="0.5" r="0.5">
          <stop offset="0" stop-color="#cadeef" stop-opacity="0.95"/>
          <stop offset="1" stop-color="#e8f1f8" stop-opacity="0"/>
        </radialGradient>
        <radialGradient id="deep-wash" cx="0.5" cy="0.5" r="0.5">
          <stop offset="0" stop-color="#0054aa" stop-opacity="0.85"/>
          <stop offset="1" stop-color="#0677ba" stop-opacity="0"/>
        </radialGradient>
        <radialGradient id="sun-wash" cx="0.5" cy="0.5" r="0.5">
          <stop offset="0" stop-color="#fff300"/>
          <stop offset="0.6" stop-color="#fefa6f" stop-opacity="0.9"/>
          <stop offset="1" stop-color="#fffec7" stop-opacity="0"/>
        </radialGradient>
        <radialGradient id="sky-wash" cx="0.5" cy="0.5" r="0.5">
          <stop offset="0" stop-color="#7badd7" stop-opacity="0.95"/>
          <stop offset="1" stop-color="#cadeef" stop-opacity="0"/>
        </radialGradient>
      </defs>

      <ellipse cx="200" cy="320" rx="230" ry="210" fill="url(#frost-wash)"/>
      <ellipse cx="600" cy="900" rx="210" ry="240" fill="url(#deep-wash)"/>
      <ellipse cx="680" cy="420" rx="150" ry="200" fill="url(#sky-wash)"/>
      <circle cx="380" cy="545" r="400" fill="url(#ring-wash)"/>
      <circle cx="385" cy="545" r="278" fill="#fffee8"/>

      <ellipse cx="70" cy="170" rx="80" ry="90" fill="url(#deep-wash)"/>
      <ellipse cx="560" cy="220" rx="150" ry="130" fill="url(#sky-wash)"/>
      <ellipse cx="200" cy="420" rx="100" ry="110" fill="url(#deep-wash)" opacity="0.7"/>
      <ellipse cx="715" cy="470" rx="70" ry="100" fill="url(#sun-wash)"/>
      <ellipse cx="95" cy="1000" rx="170" ry="190" fill="url(#sun-wash)"/>
      <ellipse cx="640" cy="1000" rx="110" ry="110" fill="url(#sun-wash)"/>
      <circle cx="75" cy="300" r="38" fill="#0054aa" opacity="0.9"/>
    </svg>

    <header class="title-block">
      <h1 class="book-title"><span class="lead">The</span>Quiet<br>Harvest</h1>
      <p class="book-subtitle">Field Notes Gathered By Many Guides for Thriving on Every Road Ahead</p>
    </header>

    <p class="publisher">The Lantern Gate Publishing House</p>
  </main>
</body>
</html>
```